Brookvale Rendering Wordpress Design

I would like a design for my friends company. He has just had his logo designed and really likes the following website.

www.tlb-rendering.co.uk

Something similar to this design would be ideal but open to additional ideas. The website shown has all the relevant content.

We have 20 years of experience and can provide a number of photos for work we have done.

More photos will be provided upon request.

Target Market(s)

Homeowners

Industry/Entity Type

Trade

Font styles to use
Sans Serif

Colors
3176b5
85cae6
85abd2
eaf1f7

Requirements
Must have
• look at www.tlb-rendering.co.uk
Nice to have
Should not have
• N/A

```html
<!DOCTYPE html>
<html lang="en">
<head>
<meta charset="utf-8">
<title>Brookvale Rendering</title>
<link href="https://fonts.googleapis.com/css2?family=Cinzel:wght@400;700&family=Open+Sans:ital,wght@0,400;0,600;0,700;1,400&display=swap" rel="stylesheet">
<style>
:root{
  --blue:#3176b5;
  --blue-dark:#245f97;
  --blue-light:#85cae6;
  --blue-soft:#85abd2;
  --pale:#eaf1f7;
  --ink:#333;
  --grey:#666;
  --dark:#2b2b2b;
  --circle:#3e3e3e;
  --white:#fff;
}
*{box-sizing:border-box;margin:0;padding:0}
html,body{width:1200px;height:2400px;overflow:hidden}
body{position:relative;background:var(--white);font-family:"Open Sans",Arial,sans-serif;color:var(--ink)}
h1,h2,h3{font-weight:400}
.abs{position:absolute}

/* header */
.topline{left:0;top:0;width:1200px;height:5px;background:var(--blue)}
.brand{left:140px;top:38px;display:flex;align-items:center;gap:12px}
.brand-mark{width:26px;height:26px;background:var(--blue)}
.brand-name{font-family:"Cinzel",Georgia,serif;font-size:34px;color:#4a5563;font-weight:400;letter-spacing:1px}
.social{top:64px;width:32px;height:32px;border-radius:50%;background:#4d4d4d}
.call-icon{left:880px;top:60px;width:38px;height:38px;border:3px solid var(--blue);border-radius:50%}
.call-label{left:926px;top:60px;font-family:"Cinzel",serif;font-size:14px;letter-spacing:1px;color:#333}
.call-number{left:926px;top:76px;font-family:"Cinzel",serif;font-size:23px;color:#222}

/* nav */
.nav{left:0;top:120px;width:1200px;height:46px;background:var(--blue)}
.nav-item{top:0;height:46px;line-height:46px;text-align:center;font-family:"Cinzel",serif;font-size:19px;color:var(--white);letter-spacing:1px;border-right:1px solid rgba(255,255,255,.25)}
.nav-item.active{background:#5b9fdb}

/* hero */
.hero{left:0;top:166px;width:1200px;height:469px;background:linear-gradient(90deg,#6f6f6f 0%,#8a8a8a 45%,#a7a39a 72%,#6e7a8a 100%)}
.callback{left:131px;top:221px;width:416px;height:281px;background:rgba(20,20,20,.78);border:1px solid rgba(255,255,255,.5);border-radius:8px}
.callback-title{left:20px;top:12px;font-family:"Cinzel",serif;font-size:21px;line-height:24px;color:var(--white)}
.callback hr{position:absolute;left:0;top:64px;width:100%;border:0;border-top:1px solid rgba(255,255,255,.35)}
.field{height:29px;background:var(--white);border-radius:3px;font-size:13px;color:#444;padding:6px 8px}
.captcha{left:20px;top:164px;font-family:Georgia,serif;font-style:italic;font-size:22px;color:#ddd}
.callback .rule2{position:absolute;left:0;top:210px;width:100%;border-top:1px solid rgba(255,255,255,.35)}
.btn{background:var(--blue);color:var(--white);font-weight:700;text-align:center;border-radius:2px}
.or-call{left:155px;top:238px;font-size:14px;font-weight:700;color:var(--white)}
.or-call-num{left:258px;top:230px;font-family:"Cinzel",serif;font-size:25px;color:var(--white)}
.hero-strip{left:0;top:558px;width:1200px;height:77px;background:rgba(49,118,181,.78);color:var(--white);text-align:center;font-weight:700;font-size:21px;line-height:32px;padding-top:6px}

/* services */
.services{left:0;top:635px;width:1200px;height:328px;background:linear-gradient(#f7f9fc,var(--pale))}
.service{top:55px;width:190px;text-align:center}
.service-ring{margin:0 auto;width:112px;height:112px;border-radius:50%;background:var(--white);box-shadow:0 2px 6px rgba(0,0,0,.15);display:flex;align-items:center;justify-content:center}
.service-disc{width:96px;height:96px;border-radius:50%;background:radial-gradient(circle at 40% 35%,#5a5a5a,var(--circle))}
.service-disc.blue{background:radial-gradient(circle at 40% 35%,#5ca7e6,var(--blue))}
.service h3{margin-top:14px;font-family:"Cinzel",serif;font-weight:400;font-size:19px;letter-spacing:1px;color:#222}
.service p{margin-top:8px;font-size:13px;line-height:18px;color:#444}
.readmore{font-size:11px;font-weight:700;color:var(--blue);text-transform:uppercase}
.service .readmore{display:block;margin-top:12px}
.divider{top:40px;width:1px;height:210px;background:#dbe3ec}

/* welcome */
.welcome-title{left:0;top:1048px;width:1200px;text-align:center;font-family:"Cinzel",serif;font-weight:400;font-size:32px;letter-spacing:1px;color:#555}
.welcome-title span{color:var(--blue)}
.welcome-copy{left:133px;top:1110px;width:522px;font-size:14.3px;line-height:24.8px;color:#333}
.video{left:691px;top:1120px;width:375px;height:251px;box-shadow:0 6px 10px rgba(0,0,0,.3)}
.video-still{width:375px;height:214px;background:linear-gradient(120deg,#5a5552,#8b6a55 45%,#a9825f 65%,#7d7f84)}
.video-bar{width:375px;height:37px;background:linear-gradient(#3b3b3b,#1b1b1b)}

/* gallery */
.gallery{left:0;top:1411px;width:1200px;height:333px;background:linear-gradient(90deg,#2f6ea9,#3f80bd 50%,#2f6ea9)}
.gallery-title{left:180px;top:52px;font-family:"Cinzel",serif;font-weight:400;font-size:28px;color:var(--white);letter-spacing:1px}
.gallery-line{left:131px;top:104px;width:938px;height:1px;background:rgba(255,255,255,.55)}
.gallery-photo{top:125px;width:233px;height:141px;border:1px solid rgba(255,255,255,.7)}
.gallery-caption{top:1554px;width:233px;text-align:center;color:var(--white);font-weight:700;font-size:15px;line-height:19px}

/* testimonials & contact */
.sec-title{font-family:"Cinzel",serif;font-weight:400;font-size:28px;color:#333;letter-spacing:1px}
.quote{left:133px;top:1840px;width:437px;height:160px;border:1px solid #bbb;border-radius:10px;padding:24px 22px 0 24px;font-style:italic;font-size:13px;line-height:21px;color:#333}
.avatar{left:157px;top:1989px;width:76px;height:76px;border-radius:50%;border:4px solid var(--white);box-shadow:0 0 0 2px #ccc;background:linear-gradient(#d9b48f,#8fa9c6)}
.client-name{left:294px;top:2026px;font-size:14px;font-weight:700;color:#333}
.contact-intro{left:624px;top:1851px;font-size:13px;color:#333}
.input{height:28px;border:1px solid #ccc;border-radius:3px;font-size:11px;color:#333;padding:6px 9px}

/* footer */
.footer{left:0;top:2120px;width:1200px;height:243px;background:var(--dark)}
.f-title{top:37px;font-family:"Cinzel",serif;font-weight:400;font-size:18px;letter-spacing:1px;color:var(--white);padding-bottom:6px;border-bottom:1px solid #555;width:125px}
.f-list{top:78px;list-style:none;font-size:13px;line-height:25px;color:#e5e5e5}
.f-list li::before{content:"›";margin-right:8px;color:#aaa}
.f-text{font-size:13px;line-height:18px;color:#e5e5e5}
.map{left:651px;top:75px;width:221px;height:114px;background:linear-gradient(135deg,#e9e4d8,#d8d3c3 50%,#ece6d2)}
.follow-dot{width:24px;height:24px;border-radius:50%;background:var(--white)}
.bottom-bar{left:0;top:2363px;width:1200px;height:37px;background:var(--blue);color:var(--white);text-align:center;font-size:12.5px;line-height:37px}
</style>
</head>
<body>

<div class="abs topline"></div>

<div class="abs brand">
  <div class="brand-mark"></div>
  <div class="brand-name">Brookvale Rendering</div>
</div>

<div class="abs social" style="left:700px"></div>
<div class="abs social" style="left:740px"></div>
<div class="abs social" style="left:780px"></div>
<div class="abs social" style="left:820px"></div>

<div class="abs call-icon">
  <svg width="32" height="32" viewBox="0 0 32 32"><path d="M10 7c1 0 2 3 3 5 0 1-2 2-2 3 1 2 3 4 5 5 1 0 2-2 3-2 2 1 5 2 5 3 0 2-2 4-4 4C13 25 7 19 7 11c0-2 2-4 3-4z" fill="#3176b5"/></svg>
</div>
<div class="abs call-label">CALL US TODAY</div>
<div class="abs call-number">020-555-0142</div>

<nav class="abs nav">
  <div class="abs nav-item active" style="left:131px;width:165px">HOME</div>
  <div class="abs nav-item" style="left:296px;width:192px">ABOUT US</div>
  <div class="abs nav-item" style="left:488px;width:184px">SERVICES</div>
  <div class="abs nav-item" style="left:672px;width:184px">GALLERY</div>
  <div class="abs nav-item" style="left:856px;width:213px">CONTACT US</div>
</nav>

<section class="abs hero" role="img" aria-label="Photograph of a plasterer in an orange cap smoothing render onto an exterior wall with a float"></section>

<form class="abs callback">
  <div class="abs callback-title">Let us call you,<br>just fill in the boxes below!</div>
  <hr>
  <div class="abs field" style="left:20px;top:75px;width:376px">Your Name</div>
  <div class="abs field" style="left:20px;top:118px;width:376px">Your Phone Number</div>
  <div class="abs captcha">5d8g6t</div>
  <div class="abs field" style="left:118px;top:164px;width:278px"></div>
  <div class="rule2"></div>
  <div class="abs btn" style="left:20px;top:232px;width:112px;height:32px;line-height:32px;font-size:17px">SUBMIT</div>
  <div class="abs or-call">Or Call Today</div>
  <div class="abs or-call-num">020-555-0142</div>
</form>

<div class="abs hero-strip">We Specialise In Internal Plastering, Rendering And Thin Coat Insulated Render<br>Systems, Serving Both The Domestic And Commercial Markets.</div>

<section class="abs services">
  <svg class="abs" style="left:58px;top:128px" width="26" height="70" viewBox="0 0 26 70"><path d="M22 2 4 35l18 33" fill="none" stroke="#888" stroke-width="2"/></svg>
  <svg class="abs" style="left:1114px;top:128px" width="26" height="70" viewBox="0 0 26 70"><path d="M4 2l18 33L4 68" fill="none" stroke="#888" stroke-width="2"/></svg>

  <div class="abs divider" style="left:303px"></div>
  <div class="abs divider" style="left:498px"></div>
  <div class="abs divider" style="left:693px"></div>
  <div class="abs divider" style="left:888px"></div>

  <div class="abs service" style="left:118px;top:55px">
    <div class="service-ring"><div class="service-disc"></div></div>
    <h3>RENDERING</h3>
    <p>Lorem ipsum dolor si amet consectetur adipiscing elit Etiam feugiat urna leo</p>
    <span class="readmore">Read More »</span>
  </div>
  <div class="abs service" style="left:310px;top:58px">
    <div class="service-ring"><div class="service-disc blue"></div></div>
    <h3>SKIMMING</h3>
    <p>Lorem ipsum dolor si amet consectetur adipiscing elit Etiam feugiat urna leo</p>
    <span class="readmore">Read More »</span>
  </div>
  <div class="abs service" style="left:505px;top:58px">
    <div class="service-ring"><div class="service-disc"></div></div>
    <h3>REPOINTING</h3>
    <p>Lorem ipsum dolor si amet consectetur adipiscing elit Etiam feugiat urna leo</p>
    <span class="readmore">Read More »</span>
  </div>
  <div class="abs service" style="left:690px;top:58px;width:210px">
    <div class="service-ring"><div class="service-disc"></div></div>
    <h3>CHIMNEY REPAIRS</h3>
    <p>Lorem ipsum dolor si amet consectetur adipiscing elit Etiam feugiat urna leo</p>
    <span class="readmore">Read More »</span>
  </div>
  <div class="abs service" style="left:895px;top:58px">
    <div class="service-ring"><div class="service-disc"></div></div>
    <h3>PLASTERBOARD</h3>
    <p>Lorem ipsum dolor si amet consectetur adipiscing elit Etiam feugiat urna leo</p>
    <span class="readmore">Read More »</span>
  </div>
</section>

<h2 class="abs welcome-title">Welcome to <span>Brookvale Rendering</span></h2>

<div class="abs welcome-copy">
  <p>Lorem ipsum dolor sit amet, consectetur adipiscing elit. Aenean sodales diamuis velit pellentesque vehicula. Donec luctus justo aliquet est volutpat, sedincidunt odio pretium. Sed id est ultrici rutrum arcu pretium, porttitor enim. Integer quis luctus ligula. Donec id scelerisque lorem. Duis vehicu nulla at tristique smper. luctus ligula. Donec id scelerisque lorem. Duis vehicu nulla at tristi smper.luctus ligula. Donec id scelerisque lorem. Duis vehicu nulla at tristique smper. Vivamus id volutpat ipsum, eget fermentum nunc. Aenean eu semperMaecenas tellus lacus, elementum vitae fringilla eget, lobortis at sapien. tristique Maecenas ultrices felis.</p>
  <p class="readmore" style="margin-top:18px">Read More »</p>
</div>

<div class="abs video">
  <div class="video-still" role="img" aria-label="Video still of a room under renovation with scaffolding against a freshly plastered wall"></div>
  <div class="video-bar">
    <svg width="375" height="37" viewBox="0 0 375 37">
      <path d="M15 13v11l9-5.5z" fill="#fff"/>
      <path d="M46 15h4l5-4v15l-5-4h-4z" fill="#fff"/>
      <rect x="72" y="16" width="206" height="5" rx="2.5" fill="#555"/>
      <rect x="72" y="16" width="96" height="5" rx="2.5" fill="#3d8fd6"/>
    </svg>
  </div>
</div>

<section class="abs gallery">
  <svg class="abs" style="left:131px;top:56px" width="32" height="26" viewBox="0 0 32 26"><rect x="6" y="1" width="24" height="18" fill="none" stroke="#fff" stroke-width="2"/><rect x="1" y="6" width="24" height="18" fill="#3f80bd" stroke="#fff" stroke-width="2"/><path d="M4 21l7-8 5 5 3-3 4 6z" fill="#fff"/></svg>
  <h2 class="abs gallery-title">Projects Gallery</h2>
  <div class="abs gallery-line"></div>
  <svg class="abs" style="left:76px;top:160px" width="26" height="70" viewBox="0 0 26 70"><path d="M22 2 4 35l18 33" fill="none" stroke="#fff" stroke-width="2"/></svg>
  <svg class="abs" style="left:1097px;top:160px" width="26" height="70" viewBox="0 0 26 70"><path d="M4 2l18 33L4 68" fill="none" stroke="#fff" stroke-width="2"/></svg>
  <div class="abs gallery-photo" style="left:133px;background:linear-gradient(#8d8378,#b3a898)" role="img" aria-label="Interior room stripped back for replastering"></div>
  <div class="abs gallery-photo" style="left:366px;background:linear-gradient(#6a5a4f,#3d3430);border:2px solid #fff" role="img" aria-label="Tudor style house with timber frame gables"></div>
  <div class="abs gallery-photo" style="left:599px;background:linear-gradient(#c2b8aa,#a48a68)" role="img" aria-label="Brick house with new render applied to the lower wall"></div>
  <div class="abs gallery-photo" style="left:832px;background:linear-gradient(#b8c4d0,#8a7058)" role="img" aria-label="Stone house under restoration"></div>
</section>
<div class="abs gallery-caption" style="left:366px">Lorem ipsum lorem ipsum<br>sit ametsit amet</div>

<svg class="abs" style="left:131px;top:1798px" width="24" height="22" viewBox="0 0 24 22"><path d="M2 2h14v10H8l-4 4v-4H2z" fill="#333"/><path d="M18 6h4v10h-2v4l-4-4h-6v-2h8z" fill="#333"/></svg>
<h2 class="abs sec-title" style="left:172px;top:1794px">Client Testimonials</h2>
<svg class="abs" style="left:525px;top:1800px" width="44" height="20" viewBox="0 0 44 20"><circle cx="9" cy="10" r="8" fill="none" stroke="#555" stroke-width="1.5"/><path d="M12 10H6m3-3-3 3 3 3" fill="none" stroke="#555" stroke-width="1.5"/><circle cx="35" cy="10" r="8" fill="none" stroke="#555" stroke-width="1.5"/><path d="M32 10h6m-3-3 3 3-3 3" fill="none" stroke="#555" stroke-width="1.5"/></svg>

<div class="abs quote">
  <span style="font-family:Georgia,serif;font-size:38px;color:#bbb;position:absolute;left:20px;top:14px">“</span>
  <p style="text-indent:32px">Lorem ipsum dolor sit amet consetug e sed diay nibh euismodl tincidunt ut laoreet dolore magam er vol wisi enim ad minim veniam quis nostrud exerci tationorem ipsum dolor sit ametee sed diammmy nibh euismd tincidunt ut laoreet dolore magna aliqur volpatl tiidunt ut laoreet dolore magna aliqur volpatl</p>
</div>
<svg class="abs" style="left:430px;top:1999px" width="110" height="36" viewBox="0 0 110 36"><path d="M0 1L10 34 109 1" fill="#fff" stroke="#bbb" stroke-width="1"/><rect x="0" y="-2" width="110" height="3" fill="#fff"/></svg>
<div class="abs avatar" role="img" aria-label="Portrait photo of the client"></div>
<div class="abs client-name">Mr. Alan Hartley</div>

<div class="abs" style="left:598px;top:1800px;width:1px;height:290px;background:#ddd"></div>

<svg class="abs" style="left:624px;top:1802px" width="24" height="18" viewBox="0 0 24 18"><rect x="1" y="1" width="22" height="16" fill="#333"/><path d="M1 1l11 9 11-9" fill="none" stroke="#fff" stroke-width="1.5"/></svg>
<h2 class="abs sec-title" style="left:664px;top:1794px">Get In Touch With Us</h2>
<div class="abs" style="left:624px;top:1840px;width:437px;height:1px;background:#bbb"></div>
<div class="abs contact-intro">Lorem ipsum dolor sit amet consectetuer adipiscing sed dmmy nibh</div>
<div class="abs input" style="left:626px;top:1885px;width:208px">Name</div>
<div class="abs input" style="left:854px;top:1885px;width:210px">Email</div>
<div class="abs input" style="left:626px;top:1926px;width:208px">Phone Number</div>
<div class="abs input" style="left:854px;top:1926px;width:210px">Service Type
  <svg class="abs" style="right:0;top:0" width="28" height="26" viewBox="0 0 28 26"><rect width="28" height="26" fill="#eee"/><path d="M9 10l5 5 5-5" fill="none" stroke="#555" stroke-width="1.5"/></svg>
</div>
<div class="abs input" style="left:626px;top:1968px;width:438px;height:64px">Your Message</div>
<div class="abs btn" style="left:626px;top:2048px;width:80px;height:27px;line-height:27px;font-size:12px">SUBMIT</div>

<footer class="abs footer">
  <h3 class="abs f-title" style="left:131px">Quick Links</h3>
  <ul class="abs f-list" style="left:131px">
    <li>Home</li><li>About Us</li><li>Services</li><li>Gallery</li><li>Contact Us</li>
  </ul>

  <h3 class="abs f-title" style="left:333px;width:238px">Contact Details</h3>
  <svg class="abs" style="left:333px;top:77px" width="12" height="16" viewBox="0 0 12 16"><path d="M6 0a6 6 0 0 0-6 6c0 4 6 10 6 10s6-6 6-10a6 6 0 0 0-6-6z" fill="#fff"/><circle cx="6" cy="6" r="2" fill="#2b2b2b"/></svg>
  <div class="abs f-text" style="left:360px;top:75px;width:220px">Lorem ipsum dolor sit consectetuer adipiscing elit, diam nonummy Lorem Ipsum - 123456</div>
  <svg class="abs" style="left:333px;top:141px" width="14" height="14" viewBox="0 0 32 32"><path d="M8 3c2 0 3 5 4 7 0 2-3 3-3 4 2 4 5 7 9 9 1 0 2-3 4-3 2 1 7 2 7 4 0 3-3 6-6 6C12 30 2 20 2 9c0-3 3-6 6-6z" fill="#fff"/></svg>
  <div class="abs f-text" style="left:360px;top:139px">020-555-0142</div>
  <svg class="abs" style="left:333px;top:183px" width="14" height="11" viewBox="0 0 14 11"><rect width="14" height="11" fill="#fff"/><path d="M0 0l7 6 7-6" fill="none" stroke="#2b2b2b" stroke-width="1.2"/></svg>
  <div class="abs f-text" style="left:360px;top:179px">info@brookvalerendering.com</div>

  <h3 class="abs f-title" style="left:651px;width:221px">Location Map</h3>
  <div class="abs map" role="img" aria-label="Street map showing the company location"></div>

  <h3 class="abs f-title" style="left:952px">Follow Us</h3>
  <div class="abs follow-dot" style="left:952px;top:75px"></div>
  <div class="abs f-text" style="left:986px;top:78px">Friendwall</div>
  <div class="abs follow-dot" style="left:952px;top:105px"></div>
  <div class="abs f-text" style="left:986px;top:108px">Chirpline</div>
  <div class="abs follow-dot" style="left:952px;top:135px"></div>
  <div class="abs f-text" style="left:986px;top:138px">Circlenet</div>
  <div class="abs follow-dot" style="left:952px;top:165px"></div>
  <div class="abs f-text" style="left:986px;top:168px">Tradelink</div>
</footer>

<div class="abs bottom-bar">Copyright © 2016 - Brookvale Rendering. All Rights Reserved.</div>

</body>
</html>
```